Covid 19 Exit Strategy one page brochure

I would like to design, and will need URGENT help, a brochure detailing a Covid 19 Exit Strategy plan. This brochure will need to be understood easily and the graphics inside should make it easy for people to understand without reading the entire text. This project is quite urgent and needs to be completed THIS WEEK - by Saturday may 16th at the latest. I am attaching two examples. I will provide the text.

```html
<!DOCTYPE html>
<html lang="en">
<head>
<meta charset="utf-8">
<title>Covid-19 Phased Exit Strategy</title>
<link href="https://fonts.googleapis.com/css2?family=Montserrat:wght@600;700;800&family=Open+Sans:wght@400;600;700&display=swap" rel="stylesheet">
<style>
:root{
  --blue:#2a3f9e;
  --blue-deep:#233591;
  --yellow:#f6d33c;
  --teal:#2f7f93;
  --orange:#d8542a;
  --green:#4d7a4c;
  --ink:#2d2d3a;
  --muted:#5a5a68;
  --paper:#ffffff;
  --canvas:#e9e9ec;
  --rule:#d9dbe3;
}
*{box-sizing:border-box;margin:0;padding:0}
html,body{width:1200px;height:2301px;overflow:hidden;background:var(--canvas)}
body{font-family:"Open Sans",Arial,sans-serif;color:var(--ink);position:relative}
.page{position:absolute;left:210px;width:780px;height:1100px;background:var(--paper);box-shadow:0 2px 10px rgba(0,0,0,.12);overflow:hidden}
.page--front{top:33px}
.page--back{top:1167px}

/* front header */
.hero{position:absolute;left:0;top:0;width:100%;height:312px;background:radial-gradient(circle at 20% 30%,#3148ab 0,var(--blue) 55%,var(--blue-deep) 100%);text-align:center;color:#fff}
.logo-box{position:absolute;left:334px;top:36px;width:112px;height:50px;background:#dfe3f4;color:var(--blue);font:700 22px "Montserrat",sans-serif;display:flex;align-items:center;justify-content:center;letter-spacing:1px}
.title{position:absolute;left:0;right:0;top:96px;font:800 112px/1 "Montserrat",sans-serif;color:var(--yellow);letter-spacing:-2px;display:flex;justify-content:center;align-items:center}
.title .virus{display:inline-block;width:96px;height:96px;border-radius:50%;background:radial-gradient(circle,#fbe36a 0,var(--yellow) 60%,#d9b421 100%);margin:0 4px}
.title .num{color:#fff}
.subtitle{position:absolute;left:0;right:0;top:225px;font:700 30px "Montserrat",sans-serif;letter-spacing:1px}
.byline{position:absolute;left:0;right:0;top:264px;font:400 21px "Open Sans",sans-serif;color:var(--yellow)}
.intro{position:absolute;left:42px;right:42px;top:328px;font-size:9.4px;line-height:1.55;color:var(--muted)}
.intro strong{color:var(--blue)}
.req-heading{position:absolute;left:243px;top:432px;width:294px;height:44px;border-top:1px solid var(--rule);border-bottom:1px solid var(--rule);text-align:center;font:800 18px/44px "Montserrat",sans-serif;color:var(--blue)}
.req-list{position:absolute;left:72px;right:56px;top:496px;list-style:none}
.req-list li{height:62px;display:flex;align-items:center;border-bottom:1px solid var(--rule);font-size:9.4px;line-height:1.4;color:var(--ink)}
.req-list svg{width:40px;height:40px;flex:none;margin:0 46px 0 22px;stroke:var(--blue);fill:none;stroke-width:1.6}

/* footer */
.footer{position:absolute;left:0;bottom:0;width:100%;height:44px;background:var(--blue);color:#fff;font:700 11px "Montserrat",sans-serif;display:flex;align-items:center}
.footer .contact{position:absolute;left:0;top:0;height:44px;width:168px;background:var(--yellow);color:var(--blue);clip-path:polygon(0 0,100% 0,86% 100%,0 100%);padding-left:48px;line-height:44px}
.footer .item{position:absolute;top:0;line-height:44px;display:flex;align-items:center;gap:8px}
.footer svg{width:12px;height:12px;fill:#fff}

/* back */
.plan-pill{position:absolute;left:219px;top:21px;width:342px;height:34px;border-radius:10px;background:var(--blue);color:#fff;text-align:center;font:800 11px/34px "Montserrat",sans-serif}
.stage{position:absolute;top:69px;width:244px;border:1px solid #cfd2da;border-top:none}
.stage--1{left:16px;height:980px}
.stage--2{left:269px;height:940px}
.stage--3{left:522px;height:780px}
.stage h2{height:28px;color:#fff;text-align:center;font:700 10px/28px "Montserrat",sans-serif}
.stage--1 h2{background:var(--teal)}
.stage--2 h2{background:var(--orange)}
.stage--3 h2{background:var(--green)}
.stage .lead{padding:8px 8px 6px;font-size:8.4px;line-height:1.2}
.stage ul{list-style:none;padding:0 8px}
.stage li{position:relative;padding-left:26px;font-size:8.4px;line-height:1.18;margin-bottom:8px;min-height:18px}
.stage li::before{content:"";position:absolute;left:0;top:1px;width:17px;height:17px;border-radius:50%;background:var(--blue)}
.back-logo{position:absolute;left:574px;top:953px;width:140px;height:80px;border-right:1px solid var(--rule);border-bottom:1px solid var(--rule);color:var(--blue);font:700 28px/80px "Montserrat",sans-serif;text-align:center}
</style>
</head>
<body>

<section class="page page--front">
  <header class="hero">
    <div class="logo-box">LOGO</div>
    <h1 class="title">C<span class="virus" role="img" aria-label="Coronavirus particle illustration"></span>VID<span class="num">-19</span></h1>
    <p class="subtitle">PHASED EXIT STRATEGY</p>
    <p class="byline">Developed by Lena Varga</p>
  </header>

  <p class="intro"><strong>Pandemics have, historically, seen their end both medically</strong> - via herd immunity or immunizations. And while there are several clinical trials underway for potential Covid-19 vaccines, we are still a long way from deploying an effective vaccine and one that will stand the test of time as the virus changes. Covid-19 pandemic will be considered 'ended' when there are only occasional traces of localized cases that are quickly contained in specific locations. Today and in the absence of an effective vaccine(s) and for the re-opening of the economies and social activities to be successful, it is critical that the following basic conditions be in place before any lockdowns are lifted and before social activities resume:</p>

  <h2 class="req-heading">GENERAL REQUIREMENTS</h2>

  <ul class="req-list">
    <li><svg viewBox="0 0 40 40"><circle cx="20" cy="20" r="16"/><path d="M12 15l7 7 4-4 5 6M24 24h4v-4"/></svg>Single digit downward trend of documented cases within the past 14-days.</li>
    <li><svg viewBox="0 0 40 40"><path d="M6 26h28M8 26v8M32 26v8M10 22h22v4H10zM14 18a3 3 0 1 0 0.1 0M20 10h6M23 7v6"/></svg>Hospitals and the health care system are capable of treating patients without operating on a crisis mode.</li>
    <li><svg viewBox="0 0 40 40"><path d="M10 34h20M14 30h12M20 30V18M16 10l8 8M22 8l6 6-4 4-6-6z"/><circle cx="14" cy="22" r="4"/></svg>Ability to screen and test symptomatic individuals within 24 hours of identification. Increased and sufficient testing capacity, to test at least 50% of all population if necessary within a timeframe of 3 months.</li>
    <li><svg viewBox="0 0 40 40"><path d="M34 20a14 14 0 1 1-4-10M30 4v6h-6"/><text x="11" y="24" font-size="10" font-weight="700" fill="#2a3f9e" stroke="none" font-family="Montserrat,sans-serif">24h</text></svg>Ability to surge ICU capacity on a short notice - 24h.</li>
    <li><svg viewBox="0 0 40 40"><path d="M14 6v20a5 5 0 1 0 4 0V6a2 2 0 0 0-4 0zM26 10l6 6M32 10l-6 6M29 8v10"/><circle cx="30" cy="28" r="4"/></svg>Ability to track and trace infected patients and contacts on a live basis and across the country and ability to react quickly to any unusual trends or outbreaks.</li>
    <li><svg viewBox="0 0 40 40"><circle cx="12" cy="10" r="3"/><path d="M7 20a5 5 0 0 1 10 0"/><circle cx="28" cy="16" r="3"/><path d="M23 26a5 5 0 0 1 10 0"/><circle cx="14" cy="28" r="3"/><path d="M9 38a5 5 0 0 1 10 0M18 12l6 3"/></svg>Plan in place to trigger targeted or full-scale containment in case of sudden outbreaks</li>
    <li><svg viewBox="0 0 40 40"><circle cx="20" cy="12" r="6"/><path d="M8 34a12 12 0 0 1 24 0zM14 14h12v4H14z"/></svg>Mandatory use of masks (at least surgical grade) for everyone in all public areas and at work. Mandatory use of N95, or equivalent, masks for all healthcare front workers and for all government agencies and authorities that are involved in overseeing the containment activities.</li>
    <li><svg viewBox="0 0 40 40"><path d="M14 6h12v8H14zM18 14v4M6 30l8-4h8l6-4 4 2-10 10H6z"/></svg>Mandatory sanitation in all places - use of disinfection available on a large scale.</li>
    <li><svg viewBox="0 0 40 40"><circle cx="14" cy="8" r="3"/><circle cx="26" cy="8" r="3"/><path d="M9 18a5 5 0 0 1 10 0M21 18a5 5 0 0 1 10 0M6 30l8-4h8l6-4 4 2-10 10H6z"/></svg>Mandatory daily checks of body temperature for everyone at the workplace or entering public areas.</li>
  </ul>

  <footer class="footer">
    <span class="contact">CONTACT US</span>
    <span class="item" style="left:222px"><svg viewBox="0 0 12 12"><path d="M2 1h3l1 3-2 1a7 7 0 0 0 3 3l1-2 3 1v3c-6 0-9-3-9-9z"/></svg>012-555-0148</span>
    <span class="item" style="left:400px"><svg viewBox="0 0 12 12"><path d="M0 2h12v8H0zM0 2l6 5 6-5" stroke="#2a3f9e" stroke-width="1"/></svg>info@lenavarga.com</span>
    <span class="item" style="left:608px"><svg viewBox="0 0 12 12"><circle cx="6" cy="6" r="6"/></svg>lenavarga.com</span>
  </footer>
</section>

<section class="page page--back">
  <div class="plan-pill">PHASED COVID-19 LOCKDOWN EXIT STRATEGY PLAN</div>

  <article class="stage stage--1">
    <h2>STAGE 1</h2>
    <p class="lead">To enter this stage, additional to the general requirements, the Effective Reproduction Number (Rt) must be less than 1 and the death rate at less than 3%.<br>The economy and social activities can resume in this sequence</p>
    <ul>
      <li>Elderly (60+ years old) and vulnerable individuals should continue to self-isolate.</li>
      <li>Social distancing should continue to be re-enforced in public areas, at work and in all areas reopened.</li>
      <li>Small businesses (300 people and less) can reopen as well with the same conditions as large businesses.</li>
      <li>No more than 5 people maximum gathering at a time in public areas and at work.</li>
      <li>Non-essential travel should be minimized between cities and regions (and within cities and regions where covid-19 infections are still a risk)</li>
      <li>Commercial shops can reopen. Shops should control the flow of people in their facilities not to exceed 30% at a time of standard capacity. Shops should provide disinfectant and temperature control at entry.</li>
      <li>Work from home should continue whenever and as much as possible.</li>
      <li>All schools should remain closed. On-line courses should continue be the preferred method for education.</li>
      <li>Religious sites can reopen with a maximum capacity of 30% or less. Social distancing and wearing masks is mandatory. Religious sites should organize (volunteers can help) to check body temperature of everyone accessing the site and provide disinfectant at entry.</li>
      <li>Hotels &amp; tourism (museums, etc.) can reopen but must operate at 30% or less capacity. All common areas (restaurants, gyms, swimming pools, conference rooms, etc.) should remain closed.</li>
      <li>Large scale events (cinema, theaters, sport, business conferences, etc.) should remain closed or operate virtually. Sport events can resume but without spectators. Athletes and the staff surrounding them should be tested, disinfectants should be available and masks used as much as reasonably possible.</li>
      <li>Transportation (buses, taxis, airlines) will resume progressively. No air travels permitted in and out of Covid-19 known hotspots, locally or internationally. Entry to country should be limited and strictly controlled. All landing passengers and visitors regardless of the country of origin should be tested for Covid-19 at arrival. All passengers and visitors will undergo a temperature check at arrival. No more than 3 people at a time in a taxi/rideshare including the driver. All passengers wearing</li>
      <li>Coffee &amp; restaurants can reopen but must operate at 30% capacity as well and comply with social distancing. Clients must wear as much as possible their masks if they are not consuming food/coffee. Clients should avoid to talking to each other with masks off.</li>
      <li>Large businesses (300 people and more, manufacturing, services, etc.) can reopen progressively. Common areas should remain closed (cafeteria, restaurant, gym, meeting rooms of no more than 5 people).</li>
      <li>Pharmacies will continue to be open. However, they must make available disinfectant for use by clients and will continue to comply with social distancing.</li>
    </ul>
  </article>

  <article class="stage stage--2">
    <h2>STAGE 2</h2>
    <p class="lead">To enter stage 2 of the Covid-19 Exit Strategy, compliance to the general requirements is compulsory, additional to a successful Stage 1 outcome. The Effective Reproduction Number (Rt) for Stage 2 must be less than 0.5 and the death rate stabilized at less than 1.5%.</p>
    <ul>
      <li>Elderly (60+ years old) and vulnerable individuals should continue to self-isolate as much as possible.</li>
      <li>No more than 10 people maximum gathering at a time in public areas and at work.</li>
      <li>Work from home should if possible or for jobs that do not have to be necessarily in an office setup.</li>
      <li>Social distancing can be relaxed. However people should continue to wear masks and use disinfectants.</li>
      <li>Travel can resume between cities and regions. The same containment restrictions should apply to any existing hotspot.</li>
      <li>Travel can resume between cities and regions. The lective surgeries can resume in hospitals and clinics that are equipped to comply with all general requirements. The same containment restrictions should apply to any existing hotspot.</li>
      <li>Large businesses (300 people and more, manufacturing, services, etc.) will continue to operate. Common areas should open but social distancing should remain (cafeteria, restaurant, gym, meeting rooms of no more than 10 people).</li>
      <li>Small businesses (300 people and less) will continue to operate with the same conditions as large businesses.</li>
      <li>Commercial shops will continue to be open and can operate at 50% capacity. Wear of masks should continue.</li>
      <li>Pharmacies will continue to be open and will need to operate a 50% capacity</li>
      <li>Transportation (buses, taxis, and airlines) will continue to operate. Still no air travels permitted in and out of Covid-19 known hotspots, locally or internationally. Entry to country should be relaxed but remain controlled. Airports should continue to use thermo cameras to monitor passenger's temperature at landing. Airports should be equipped to test for Covid-19 if necessary. Transportation by taxi/rideshare continues, however, passengers wear masks. Buses could operate with 50% capacity per bus.</li>
      <li>Religious sites can operate with a maximum capacity of 50%. Social distancing and wearing masks should be enforced. Sites should continue to check body temperature of everyone accessing the site and provide disinfectant at entry.</li>
      <li>Hotels &amp; tourism (museums, etc.) can operate at 50% capacity. All common areas (restaurants, gyms, swimming pools, conference rooms, etc.) could reopen. Gatherings are limited to 10 people or less and can be expanded with social distancing and wearing protective masks.</li>
      <li>Coffee &amp; restaurants can operate at 50% capacity and continue comply with social distancing. Clients must wear as much as possible their masks if they are not consuming food/coffee.</li>
      <li>Schools can reopen in parallel with on-line education. Social distancing and re-arranging school seating to prevent the spread of infection is mandatory.</li>
      <li>Large scale events (cinema, theaters, sport, business conferences, etc.) could resume under strict social distancing. People should wear masks.</li>
    </ul>
  </article>

  <article class="stage stage--3">
    <h2>STAGE 3</h2>
    <p class="lead">To enter stage 3 of the Covid-19 Exit Strategy, compliance to the general requirements is compulsory, additional to a successful Stage 2 outcome. The Effective Reproduction Number (Rt) for Stage 3 must be less than 0.3 and the death rate stabilized at less than 1%.</p>
    <ul>
      <li>Elderly (60+ years old) and vulnerable individuals may resume all previously exercised activities without restrictions.</li>
      <li>Restrictions as to the number of people gathering together can be lifted. Social distancing can be relaxed. However, wear of masks may continue.</li>
      <li>Travel can resume between cities and regions and out of country travel. The same containment restrictions as Stage 1 and 2 would continue to apply to any existing hotspot.</li>
      <li>All hospital and clinic surgeries can resume in hospitals in compliance with standard hospital and health care procedures.</li>
      <li>Large businesses (300 people and more, manufacturing, services, etc.) will resume normal operations. Clients may wear masks for personal protection if they wish to.</li>
      <li>Small businesses (300 people and less) will operate with the same conditions as large businesses.</li>
      <li>Commercial shops can operate on a normal mode - previous to covid-19. Wear of masks could be recommended in certain areas.</li>
      <li>Pharmacies can operate at a normal state.</li>
      <li>Transportation (buses, taxis, and airlines) will operate at a normal capacity. Still no air travels permitted in and out of Covid-19 known hotspots, locally or internationally. Entry to country should be relaxed and operate normally. Airports should continue to use thermo cameras to monitor passenger's temperature at landing. Airports should be equipped to test for Covid-19 if necessary. Transportation by taxi/rideshare and buses will resume on a normal mode. Wear of masks is elective.</li>
      <li>Religious sites can operate normally. Wear of masks should be elective.</li>
      <li>Hotels &amp; tourism (museums, etc.) can operate at 100% capacity including all common areas.</li>
      <li>Coffee &amp; restaurants can resume normal operations. Clients may wear masks for personal protection if they wish to.</li>
      <li>Schools can resume operations. Re-arranging school seating should continue until a vaccine is found.</li>
      <li>Large scale events (cinema, theaters, sport, business conferences, etc.) could resume under moderate social distancing. People may elect to wear masks.</li>
    </ul>
  </article>

  <div class="back-logo">LOGO</div>

  <footer class="footer">
    <span class="contact">CONTACT US</span>
    <span class="item" style="left:222px"><svg viewBox="0 0 12 12"><path d="M2 1h3l1 3-2 1a7 7 0 0 0 3 3l1-2 3 1v3c-6 0-9-3-9-9z"/></svg>012-555-0148</span>
    <span class="item" style="left:400px"><svg viewBox="0 0 12 12"><path d="M0 2h12v8H0zM0 2l6 5 6-5" stroke="#2a3f9e" stroke-width="1"/></svg>info@lenavarga.com</span>
    <span class="item" style="left:608px"><svg viewBox="0 0 12 12"><circle cx="6" cy="6" r="6"/></svg>lenavarga.com</span>
  </footer>
</section>

</body>
</html>
```